Solar appointment reminder card

We are looking for a new design for our appointment reminder card since we have changed our logo. The card should have the new logo along with space for the employee to hand write the customers appointment date, time, the employees name and phone number.
I've uploaded what our old basic appointment card looked like and our new logo.

The cards should be in a standard business card size and could be horizontal or vertical.

```html
<!DOCTYPE html>
<html lang="en">
<head>
<meta charset="utf-8">
<title>Hudson Bright Solar – Appointment Card</title>
<link href="https://fonts.googleapis.com/css2?family=Montserrat:wght@600;700;800&display=swap" rel="stylesheet">
<style>
  :root{
    --stage:#f3a623;
    --ink:#000000;
    --sun:#f2bf2c;
    --amber:#e98a23;
    --paper:#f1f1f1;
    --field:#e6e6e7;
    --rule:#111111;
  }
  *{box-sizing:border-box;margin:0;padding:0}
  html,body{width:1200px;height:1000px;overflow:hidden}
  body{background:var(--stage);font-family:"Montserrat",Arial,sans-serif;position:relative;color:var(--ink)}
  .card{position:absolute;top:226px;width:342px;height:598px;border-radius:18px;overflow:hidden;background:var(--paper)}
  .card--front{left:248px}
  .card--back{left:647px}
  .band{position:absolute;left:0;width:100%}
  .band--ink{background:var(--ink)}
  .band--sun{background:var(--sun)}
  .band--amber{background:var(--amber);display:flex;align-items:center;justify-content:center;font-weight:700;font-size:17px;letter-spacing:.3px}
  .band--field{background:var(--field)}
  .brand{position:absolute;left:0;width:100%;display:flex;align-items:center;justify-content:center;gap:14px}
  .brand__dot{width:60px;height:60px;border-radius:50%;background:var(--sun);flex:none}
  .brand__name{color:var(--amber);font-weight:700;line-height:1}
  .brand__short{font-size:62px;letter-spacing:-1px}
  .brand__long{font-size:13px;letter-spacing:1.4px;margin-top:6px}
  .tab{position:absolute;left:24px;width:288px;height:48px;background:var(--sun);border-radius:0 0 16px 16px;display:flex;align-items:center;justify-content:center;font-weight:700;font-size:24px;letter-spacing:1.6px}
  .title{position:absolute;left:0;top:0;width:100%;height:83px;background:var(--sun);display:flex;align-items:center;justify-content:center;font-weight:700;font-size:35px;letter-spacing:.8px}
  .field{position:absolute;display:flex;align-items:flex-end;font-weight:700;font-size:16px}
  .field__line{flex:1;border-bottom:2px solid var(--rule);margin-left:10px;margin-bottom:4px}
  .phone-pill{position:absolute;left:20px;top:524px;width:299px;height:40px;border-radius:20px;background:var(--paper)}
  .phone-icon{position:absolute;width:40px;height:40px;border-radius:50%;background:var(--ink);display:flex;align-items:center;justify-content:center}
  .phone-icon svg{width:20px;height:20px}
  .phone-stub{position:absolute;left:0;top:352px;width:36px;height:24px;background:var(--sun)}
  .phone-line{position:absolute;left:66px;top:364px;width:250px;border-bottom:2px solid var(--rule)}
</style>
</head>
<body>

<section class="card card--front">
  <div class="band band--ink" style="top:0;height:196px"></div>
  <div class="brand" style="top:58px">
    <span class="brand__dot"></span>
    <div class="brand__name"><div class="brand__short">HBS</div><div class="brand__long">HUDSON BRIGHT SOLAR</div></div>
  </div>
  <div class="band band--sun" style="top:196px;height:10px"></div>
  <div class="tab" style="top:198px">APPOINTMENT</div>
  <div class="field" style="left:17px;top:286px;width:302px">DATE<span class="field__line"></span></div>
  <div class="field" style="left:17px;top:332px;width:302px">TIME<span class="field__line"></span></div>
  <div class="band band--amber" style="top:386px;height:35px">REPRESENTATIVE</div>
  <div class="band band--field" style="top:421px;height:66px"></div>
  <div class="band band--sun" style="top:487px;height:111px"></div>
  <div class="phone-pill"></div>
  <div class="phone-icon" style="left:20px;top:524px">
    <svg viewBox="0 0 24 24"><path fill="#f2bf2c" d="M6.6 10.8a15 15 0 0 0 6.6 6.6l2.2-2.2a1 1 0 0 1 1-.25 11.4 11.4 0 0 0 3.6.57 1 1 0 0 1 1 1V20a1 1 0 0 1-1 1A17 17 0 0 1 3 4a1 1 0 0 1 1-1h3.5a1 1 0 0 1 1 1c0 1.25.2 2.45.57 3.57a1 1 0 0 1-.25 1z"/></svg>
  </div>
</section>

<section class="card card--back">
  <div class="title">APPOINTMENT</div>
  <div class="field" style="left:17px;top:120px;width:305px">DATE<span class="field__line"></span></div>
  <div class="field" style="left:17px;top:176px;width:305px">TIME<span class="field__line"></span></div>
  <div class="band band--amber" style="top:230px;height:24px">REPRESENTATIVE</div>
  <div class="band band--field" style="top:254px;height:67px"></div>
  <div class="phone-stub"></div>
  <div class="phone-icon" style="left:20px;top:344px">
    <svg viewBox="0 0 24 24"><path fill="#f2bf2c" d="M6.6 10.8a15 15 0 0 0 6.6 6.6l2.2-2.2a1 1 0 0 1 1-.25 11.4 11.4 0 0 0 3.6.57 1 1 0 0 1 1 1V20a1 1 0 0 1-1 1A17 17 0 0 1 3 4a1 1 0 0 1 1-1h3.5a1 1 0 0 1 1 1c0 1.25.2 2.45.57 3.57a1 1 0 0 1-.25 1z"/></svg>
  </div>
  <div class="phone-line"></div>
  <div class="band band--ink" style="top:402px;height:196px"></div>
  <div class="brand" style="top:464px">
    <span class="brand__dot"></span>
    <div class="brand__name"><div class="brand__short">HBS</div><div class="brand__long">HUDSON BRIGHT SOLAR</div></div>
  </div>
</section>

</body>
</html>
```